Business Card and Stationary Design

After the successful redesign of our logo we are wanting to follow suite and create a new business card and stationary design!

New Logo is attached, information required on the business card should contain a mixture of the following but layout/arrangement is up to the designer.

Happy if the national provider number and abn are on the back, and happy for them to be smaller than the rest.

I am also happy to receive single sided or weird and wonderful designs.

Name
Title
National Provider Number 7291
ABN 53 219 864 317
Level 3, 42 Marlow Street
Kotara Vale NSW 2291
Ph: 1300 987 214
Mobile: 0432 785 619
name@ferngatebuild.com.au
www.ferngatebuild.com.au

Target Market(s)

Professionals, Peers, Students, Suppliers...

Industry/Entity Type

Construction

Contact Information for Business Card

Listed in project description

Font styles to use
Other font styles liked:
• Century Gothic

Colors
0455a3
3176b5
ffffff

Requirements
Must have
• Professional Design, same color scheme as our logo
Nice to have
• Something that sets our apart from everyone else would be fantastic, open to size and shape and layout options, as long as they present professionally.
• Open to raised/embossed text, alternative materials, custom sizes, clear material
Should not have
• The color orange

```html
<!DOCTYPE html>
<html lang="en">
<head>
<meta charset="utf-8">
<title>Ferngate Build – Business Card</title>
<link rel="stylesheet" href="https://fonts.googleapis.com/css2?family=Roboto:ital,wght@0,400;0,500;0,700;1,400&display=swap">
<style>
  :root {
    --page-bg: #d9dbdf;
    --card-top: #f4f5f7;
    --card-bottom: #e4e6ea;
    --navy: #1f2b63;
    --ink: #3a3d44;
    --muted: #5a5d64;
    --band-text: #b9c2dc;
  }
  * { box-sizing: border-box; margin: 0; padding: 0; }
  html, body {
    width: 1200px; height: 969px; overflow: hidden;
    background: var(--page-bg);
    font-family: "Roboto", Arial, sans-serif;
  }
  .card {
    position: absolute; left: 100px; top: 200px;
    width: 1000px; height: 566px;
    background: linear-gradient(160deg, var(--card-top), var(--card-bottom));
    border: 1px solid rgba(255,255,255,0.8);
    box-shadow: 0 8px 28px rgba(0,0,0,0.12);
    color: var(--ink);
  }
  .brand {
    position: absolute; right: 44px; top: 50px;
    display: flex; align-items: center; gap: 16px;
  }
  .brand-square { width: 54px; height: 54px; background: var(--navy); }
  .brand-name { font-size: 50px; font-weight: 400; color: var(--navy); line-height: 1; }
  .tagline {
    position: absolute; right: 44px; top: 122px;
    font-size: 15px; font-weight: 700; color: var(--navy); letter-spacing: 0.6px;
  }
  .person-name {
    position: absolute; left: 55px; top: 160px;
    font-size: 32px; font-weight: 700; color: var(--navy);
  }
  .person-title { position: absolute; left: 55px; top: 205px; font-size: 24px; color: var(--muted); }
  .address { position: absolute; left: 55px; top: 254px; font-size: 24px; line-height: 30px; }
  .contacts { position: absolute; left: 55px; top: 332px; list-style: none; font-size: 23px; }
  .contacts li { display: flex; align-items: center; gap: 14px; height: 32px; }
  .contacts svg { width: 22px; height: 22px; fill: var(--navy); flex: none; }
  .registration { position: absolute; left: 55px; top: 430px; font-size: 23px; line-height: 30px; }
  .web-band {
    position: absolute; left: 0; top: 512px; width: 940px; height: 32px;
    background: var(--navy);
    display: flex; align-items: center; justify-content: center;
  }
  .web-band span {
    font-size: 21px; font-style: italic; letter-spacing: 7px; color: var(--band-text);
  }
</style>
</head>
<body>
  <article class="card">
    <header class="brand">
      <div class="brand-square"></div>
      <div class="brand-name">ferngate build</div>
    </header>
    <p class="tagline">DESIGN • BUILD • RENOVATE • MAINTAIN</p>

    <h1 class="person-name">DANIEL REYES</h1>
    <p class="person-title">CEO/FOUNDER</p>

    <p class="address">Level 3, 42 Marlow Street<br>Kotara Vale NSW 2291</p>

    <ul class="contacts">
      <li>
        <svg viewBox="0 0 24 24" aria-hidden="true"><path d="M6.6 10.8c1.4 2.8 3.8 5.1 6.6 6.6l2.2-2.2c.3-.3.7-.4 1-.2 1.1.4 2.3.6 3.6.6.6 0 1 .4 1 1V20c0 .6-.4 1-1 1C10.6 21 3 13.4 3 4c0-.6.4-1 1-1h3.5c.6 0 1 .4 1 1 0 1.3.2 2.5.6 3.6.1.3 0 .7-.2 1l-2.3 2.2z"/></svg>
        1300 987 214
      </li>
      <li>
        <svg viewBox="0 0 24 24" aria-hidden="true"><path d="M7 1h10a2 2 0 0 1 2 2v18a2 2 0 0 1-2 2H7a2 2 0 0 1-2-2V3a2 2 0 0 1 2-2zm0 3v14h10V4H7zm5 15.2a1.1 1.1 0 1 0 0 2.2 1.1 1.1 0 0 0 0-2.2z"/></svg>
        0432 785 619
      </li>
      <li>
        <svg viewBox="0 0 24 24" aria-hidden="true"><path d="M3 6h18v12H3V6zm2 2v.3l7 4.5 7-4.5V8H5zm0 2.7V16h14v-5.3l-7 4.5-7-4.5z"/></svg>
        name@ferngatebuild.com.au
      </li>
    </ul>

    <p class="registration">National Provider Number 7291<br>ABN 53 219 864 317</p>

    <footer class="web-band"><span>www.ferngatebuild.com.au</span></footer>
  </article>
</body>
</html>
```